Vymar Life Sciences is a Company providing consultancy services to companies operating within the Life Sciences Industry; namely pharmaceutical and Medical Devices. Vymar stands for Quality and Growth; since we mainly provide Quality related consultancy but our approach is to help companies Grow. Thus Business Development is another area we focus on.
We do have the logos for our company now we are lookign for a professional slide deck to use for our ppts.

```html
<!DOCTYPE html>
<html lang="en">
<head>
<meta charset="utf-8">
<title>Vymar Life Sciences – Slide Deck</title>
<link href="https://fonts.googleapis.com/css2?family=Open+Sans:wght@400;600;700&display=swap" rel="stylesheet">
<style>
  :root{
    --canvas:#e8e4e3;
    --green:#0d2e2a;
    --orange:#f39800;
    --orange-soft:#fbd89b;
    --amber:#d99a00;
    --ink:#333;
    --muted:#666;
    --rule:#cfcfcf;
  }
  html,body{margin:0;padding:0;width:1200px;height:1200px;overflow:hidden;background:var(--canvas);}
  .deck{position:relative;width:1200px;height:1200px;}
  .slide{position:absolute;width:274px;height:154px;display:block;}
  .slide text{font-family:'Open Sans',sans-serif;}
  .dk{fill:var(--green);} .or{fill:var(--orange);} .wh{fill:#fff;}
  .ink{fill:var(--ink);} .mu{fill:var(--muted);}
  .bold{font-weight:700;}
  .line-or{stroke:var(--orange);fill:none;}
  .line-dk{stroke:var(--green);fill:none;}
</style>
</head>
<body>
<div class="deck">

<svg width="0" height="0" style="position:absolute">
  <defs>
    <linearGradient id="city" x1="0" y1="0" x2="0" y2="1">
      <stop offset="0" stop-color="#4b7fb8"/><stop offset=".55" stop-color="#2a4f7d"/><stop offset="1" stop-color="#0e223c"/>
    </linearGradient>
    <linearGradient id="dusk" x1="0" y1="0" x2="0" y2="1">
      <stop offset="0" stop-color="#5a6f8f"/><stop offset=".5" stop-color="#c98a5a"/><stop offset="1" stop-color="#1c3550"/>
    </linearGradient>
    <linearGradient id="office" x1="0" y1="0" x2="1" y2="1">
      <stop offset="0" stop-color="#dfe5ea"/><stop offset="1" stop-color="#9fb0c0"/>
    </linearGradient>
    <linearGradient id="teal" x1="0" y1="0" x2="1" y2="1">
      <stop offset="0" stop-color="#0f4a5c"/><stop offset="1" stop-color="#1d6f86"/>
    </linearGradient>
    <linearGradient id="desk" x1="0" y1="0" x2="1" y2="0">
      <stop offset="0" stop-color="#cfcfcf"/><stop offset="1" stop-color="#8d8f91"/>
    </linearGradient>
  </defs>
</svg>

<!-- Row 1 -->
<svg class="slide cover" style="left:32px;top:99px" viewBox="0 0 442 248">
  <rect width="442" height="248" class="wh"/>
  <polygon role="img" aria-label="Night city skyline photo" points="0,28 252,28 140,220 0,220" fill="url(#city)"/>
  <polygon points="200,72 246,72 190,170 144,170" fill="#fff" opacity=".35"/>
  <polygon points="255,0 442,0 442,248 120,248" class="dk"/>
  <text x="418" y="62" text-anchor="end" font-size="21" class="or">PPT</text>
  <text x="418" y="90" text-anchor="end" font-size="21" class="or">templates</text>
  <text x="299" y="201" text-anchor="middle" font-size="6.5" letter-spacing="3" textLength="242" lengthAdjust="spacing" class="wh">VYMAR LIFE SCIENCES</text>
  <text x="299" y="213" text-anchor="middle" font-size="3.4" letter-spacing="1" textLength="150" lengthAdjust="spacing" class="wh">QUALITY-LED GROWTH FOR PHARMA AND DEVICES</text>
</svg>

<svg class="slide agenda" style="left:318px;top:99px" viewBox="0 0 442 248">
  <rect width="442" height="248" fill="#f3f3f3"/>
  <rect x="25" y="40" width="391" height="188" class="dk"/>
  <rect x="45" y="57" width="351" height="155" fill="none" stroke="#5d7571" stroke-width=".8"/>
  <line x1="209" y1="46" x2="233" y2="46" class="line-or" stroke-width="1.2"/>
  <g class="wh" text-anchor="middle">
    <text x="87" y="134" font-size="20">01.</text><text x="87" y="146" font-size="8">Tittle</text><text x="87" y="153" font-size="4.5">Project introduction</text>
    <text x="176" y="134" font-size="20">02.</text><text x="176" y="146" font-size="8">Tittle</text><text x="176" y="153" font-size="4.5">Project operation</text><text x="176" y="159" font-size="4.5">demonstration</text>
    <text x="265" y="134" font-size="20">03.</text><text x="265" y="146" font-size="8">Tittle</text><text x="265" y="153" font-size="4.5">Return on</text><text x="265" y="159" font-size="4.5">investment analysis</text>
    <text x="355" y="134" font-size="20">04.</text><text x="355" y="146" font-size="8">Tittle</text><text x="355" y="153" font-size="4.5">Future development</text><text x="355" y="159" font-size="4.5">planning</text>
  </g>
  <g stroke="#5d7571" stroke-width=".6"><line x1="131" y1="125" x2="131" y2="160"/><line x1="221" y1="125" x2="221" y2="160"/><line x1="310" y1="125" x2="310" y2="160"/></g>
</svg>

<svg class="slide section" style="left:606px;top:99px" viewBox="0 0 442 248">
  <rect width="442" height="248" class="wh"/>
  <polygon role="img" aria-label="Harbour city at dusk photo" points="200,0 442,0 442,130 125,130" fill="url(#dusk)"/>
  <polygon points="125,130 442,130 442,218 74,218" fill="#f2f3f4"/>
  <polygon role="img" aria-label="Glass building facade photo" points="74,218 442,218 442,248 58,248" fill="url(#teal)"/>
  <polygon points="0,0 92,0 0,160" class="dk"/>
  <polygon points="92,0 200,0 58,248 0,248 0,160" class="or"/>
  <text x="344" y="173" text-anchor="end" font-size="13" fill="#222">Tittle text</text>
  <text x="344" y="185" text-anchor="end" font-size="7.5" fill="#222">Project introduction</text>
  <rect x="350" y="138" width="66" height="66" class="dk"/>
  <text x="383" y="181" text-anchor="middle" font-size="22" class="wh">01</text>
</svg>

<svg class="slide intro" style="left:894px;top:99px" viewBox="0 0 442 248">
  <rect width="442" height="248" class="wh"/>
  <rect x="22" y="15" width="16" height="10" class="dk"/><text x="30" y="22" text-anchor="middle" font-size="4" class="wh">00</text><text x="42" y="24" font-size="8" class="ink">Heading</text>
  <rect role="img" aria-label="City skyline panorama photo" x="0" y="40" width="442" height="102" fill="url(#city)"/>
  <rect x="180" y="133" width="82" height="18" class="or"/>
  <text x="221" y="146" text-anchor="middle" font-size="10" class="wh">Tittle text</text>
  <text x="221" y="161" text-anchor="middle" font-size="4.5" class="ink">Project introduction</text>
  <g text-anchor="middle" font-size="4.5" class="mu">
    <text x="221" y="181">Add your detailed small paragraph text content here, related to the title and in line with the overall language style content please be concise, as</text>
    <text x="221" y="187">vivid as possible, you need to express the meaning clearly complete, control the number of words, and design layout in line with, to maintain</text>
    <text x="221" y="193">beautiful and generous</text>
  </g>
  <line x1="0" y1="228" x2="210" y2="228" class="line-or" stroke-width=".6"/><line x1="232" y1="228" x2="442" y2="228" class="line-or" stroke-width=".6"/>
  <circle cx="221" cy="228" r="8" class="line-or" stroke-width=".8"/>
  <rect x="218" y="224" width="6" height="8" class="line-or" stroke-width=".7"/>
</svg>

<!-- Row 2 -->
<svg class="slide team" style="left:32px;top:268px" viewBox="0 0 442 248">
  <rect width="442" height="248" class="wh"/>
  <rect x="22" y="15" width="16" height="10" class="dk"/><text x="30" y="22" text-anchor="middle" font-size="4" class="wh">00</text><text x="42" y="24" font-size="8" class="ink">Heading</text>
  <g>
    <rect role="img" aria-label="Portrait photo of team member" x="28" y="62" width="80" height="84" fill="url(#office)"/>
    <rect role="img" aria-label="Portrait photo of team member" x="130" y="62" width="80" height="84" fill="url(#office)"/>
    <rect role="img" aria-label="Portrait photo of team member" x="232" y="62" width="80" height="84" fill="url(#office)"/>
    <rect role="img" aria-label="Portrait photo of team member" x="333" y="62" width="80" height="84" fill="url(#office)"/>
    <rect x="28" y="135" width="80" height="11" class="dk"/><rect x="130" y="135" width="80" height="11" class="dk"/><rect x="232" y="135" width="80" height="11" class="dk"/><rect x="333" y="135" width="80" height="11" class="dk"/>
  </g>
  <g text-anchor="middle">
    <g font-size="5" class="wh"><text x="68" y="143">Enter the content</text><text x="170" y="143">Enter the content</text><text x="272" y="143">Enter the content</text><text x="373" y="143">Enter the content</text></g>
    <g font-size="5.5" class="ink bold"><text x="68" y="165">Add a title</text><text x="170" y="165">Add a title</text><text x="272" y="165">Add a title</text><text x="373" y="165">Add a title</text></g>
    <g font-size="4.5" class="mu">
      <text x="68" y="173">Add your detailed small</text><text x="68" y="179">paragraph text content</text><text x="68" y="185">here</text>
      <text x="170" y="173">Add your detailed small</text><text x="170" y="179">paragraph text content</text><text x="170" y="185">here</text>
      <text x="272" y="173">Add your detailed small</text><text x="272" y="179">paragraph text content</text><text x="272" y="185">here</text>
      <text x="373" y="173">Add your detailed small</text><text x="373" y="179">paragraph text content</text><text x="373" y="185">here</text>
    </g>
  </g>
</svg>

<svg class="slide metrics" style="left:318px;top:268px" viewBox="0 0 442 248">
  <rect width="442" height="248" class="dk"/>
  <rect role="img" aria-label="Business meeting with documents and tablet photo" x="222" y="0" width="220" height="248" fill="url(#office)"/>
  <circle cx="222" cy="124" r="7" class="wh"/>
  <text x="20" y="54" font-size="10" class="wh">Add the title here</text>
  <text x="20" y="61" font-size="4" class="wh">ADD THE TITLE HERE</text>
  <g font-size="4.5" class="wh" opacity=".9">
    <text x="20" y="76">Add your detailed small paragraph text content here, related to the</text>
    <text x="20" y="82">title and in line with the overall language style content please be</text>
    <text x="20" y="88">concise, as vivid as possible, you need to express the meaning</text>
    <text x="20" y="94">clearly complete, control the number of words, and design layout in</text>
    <text x="20" y="100">line with, to maintain beautiful and generous. Add your detailed</text>
    <text x="20" y="106">small paragraph text here, and be concise about the title and</text>
    <text x="20" y="112">conform to the overall language style.</text>
  </g>
  <g stroke="#8ea09c" stroke-width=".6">
    <line x1="26" y1="128" x2="26" y2="215"/><line x1="58" y1="128" x2="58" y2="215"/><line x1="87" y1="128" x2="87" y2="215"/><line x1="116" y1="128" x2="116" y2="215"/><line x1="145" y1="128" x2="145" y2="215"/><line x1="174" y1="128" x2="174" y2="215"/>
  </g>
  <g stroke="var(--orange)" stroke-width="1.2">
    <line x1="26" y1="158" x2="26" y2="215"/><line x1="58" y1="146" x2="58" y2="215"/><line x1="87" y1="180" x2="87" y2="215"/><line x1="116" y1="163" x2="116" y2="215"/><line x1="145" y1="137" x2="145" y2="215"/><line x1="174" y1="173" x2="174" y2="215"/>
  </g>
  <g font-size="4.2" class="wh">
    <text x="32" y="158">80%</text><text x="61" y="146">85%</text><text x="90" y="180">32%</text><text x="119" y="163">66%</text><text x="148" y="137">92%</text><text x="177" y="173">50%</text>
    <text x="17" y="225">2018.01</text><text x="48" y="225">2018.01</text><text x="77" y="225">2018.09</text><text x="106" y="225">2018.11</text><text x="135" y="225">20XX.01</text><text x="164" y="225">20XX.02</text>
  </g>
</svg>

<svg class="slide device" style="left:606px;top:268px" viewBox="0 0 442 248">
  <rect width="442" height="248" class="wh"/>
  <polygon points="0,248 442,0 442,248" class="dk"/>
  <rect x="22" y="15" width="16" height="10" class="dk"/><text x="30" y="22" text-anchor="middle" font-size="4" class="wh">00</text><text x="42" y="24" font-size="8" class="ink">Heading</text>
  <rect x="186" y="54" width="70" height="140" rx="9" fill="#111"/>
  <rect role="img" aria-label="Skyscrapers looking up photo" x="190" y="60" width="62" height="128" rx="5" fill="url(#city)"/>
  <g text-anchor="middle">
    <path d="M88,55 v16 M82,58 h12 l2,2 -2,2 h-12 Z M82,64 h12 v4 h-12 Z" class="line-dk" stroke-width=".9"/>
    <text x="88" y="85" font-size="5.5" class="ink bold">Add a title</text>
    <g font-size="4.5" class="mu"><text x="88" y="93">Add your detailed small paragraph</text><text x="88" y="99">text content here, related to the title</text><text x="88" y="105">and in line with the overall language</text><text x="88" y="111">style content please be concise, as</text><text x="88" y="117">vivid as possible, you need to express</text><text x="88" y="123">the meaning clearly complete,</text><text x="88" y="129">control the number of words, and</text><text x="88" y="135">design layout in line with, to</text><text x="88" y="141">maintain beautiful and generous.</text></g>
    <line x1="82" y1="162" x2="96" y2="162" stroke="#bbb" stroke-width=".5"/>
    <circle cx="342" cy="98" r="8" fill="none" stroke="#fff" stroke-width=".8"/>
    <path d="M342,92 l3,6 -3,6 -3,-6 Z" fill="none" stroke="#fff" stroke-width=".6"/>
    <text x="342" y="120" font-size="5.5" class="wh bold">Add a title</text>
    <g font-size="4.5" class="wh"><text x="342" y="128">Add your detailed small paragraph</text><text x="342" y="134">text content here, related to the title</text><text x="342" y="140">and in line with the overall language</text><text x="342" y="146">style content please be concise, as</text><text x="342" y="152">vivid as possible, you need to express</text><text x="342" y="158">the meaning clearly complete,</text><text x="342" y="164">control the number of words, and</text><text x="342" y="170">design layout in line with, to</text><text x="342" y="176">maintain beautiful and generous.</text></g>
  </g>
</svg>

<svg class="slide linechart" style="left:894px;top:268px" viewBox="0 0 442 248">
  <rect width="442" height="248" class="wh"/>
  <rect x="20" y="15" width="16" height="10" class="dk"/><text x="28" y="22" text-anchor="middle" font-size="4" class="wh">00</text><text x="40" y="24" font-size="8" class="ink">Heading</text>
  <rect x="0" y="70" width="442" height="108" class="dk"/>
  <rect x="24" y="42" width="188" height="186" class="wh" stroke="#ddd" stroke-width=".6"/>
  <g font-size="4.5" class="ink"><text x="36" y="95">6</text><text x="36" y="108">5</text><text x="36" y="121">4</text><text x="36" y="134">3</text><text x="36" y="147">2</text><text x="36" y="160">1</text><text x="36" y="173">0</text>
  <text x="58" y="182">zzz</text><text x="90" y="182">zzz</text><text x="122" y="182">zzz</text><text x="154" y="182">zzz</text></g>
  <line x1="43" y1="93" x2="43" y2="172" stroke="#999" stroke-width=".5"/><line x1="43" y1="172" x2="172" y2="172" stroke="#999" stroke-width=".5"/>
  <path d="M60,115 C80,140 95,140 110,125 S140,95 158,108" fill="none" stroke="#2e7ec2" stroke-width=".8"/>
  <path d="M60,148 C80,125 100,122 120,130 S150,118 158,100" fill="none" stroke="#2ba9a0" stroke-width=".8"/>
  <path d="M60,160 C90,140 120,125 158,105" fill="none" stroke="#e3c21a" stroke-width=".8"/>
  <g font-size="4" class="mu"><text x="188" y="127">zz</text><text x="188" y="137">zz2</text><text x="188" y="147">zz3</text></g>
  <g stroke-width=".6"><line x1="178" y1="126" x2="186" y2="126" stroke="#2e7ec2"/><line x1="178" y1="136" x2="186" y2="136" stroke="#2ba9a0"/><line x1="178" y1="146" x2="186" y2="146" stroke="#e3c21a"/></g>
  <rect x="228" y="92" width="12" height="11" fill="none" stroke="#fff" stroke-width=".6"/>
  <rect x="228" y="136" width="12" height="11" fill="none" stroke="#fff" stroke-width=".6"/>
  <g font-size="4.4" class="wh">
    <text x="246" y="95" class="bold">Add a title</text><text x="246" y="101">Add your detailed small paragraph text here, and be concise</text><text x="246" y="106">about the title and conform to the overall language style,</text><text x="246" y="111">express the meaning you need to express clearly and completely,</text><text x="246" y="116">and keep it beautiful and generous.</text>
    <text x="246" y="139" class="bold">Add a title</text><text x="246" y="145">Add your detailed small paragraph text here, and be concise</text><text x="246" y="150">about the title and conform to the overall language style,</text><text x="246" y="155">express the meaning you need to express clearly and completely,</text><text x="246" y="160">and keep it beautiful and generous.</text>
  </g>
</svg>

<!-- Row 3 -->
<svg class="slide feature-list" style="left:32px;top:438px" viewBox="0 0 442 248">
  <rect width="442" height="248" class="wh"/>
  <rect x="22" y="15" width="16" height="10" class="dk"/><text x="30" y="22" text-anchor="middle" font-size="4" class="wh">00</text><text x="42" y="24" font-size="8" class="ink">Heading</text>
  <rect x="25" y="56" width="392" height="172" fill="none" stroke="#bbb" stroke-width=".6"/>
  <rect x="41" y="40" width="139" height="175" class="or"/>
  <rect x="50" y="53" width="121" height="80" class="wh"/>
  <rect role="img" aria-label="Team presentation in office photo" x="53" y="56" width="115" height="74" fill="url(#office)"/>
  <text x="108" y="171" text-anchor="middle" font-size="10" class="wh">Enter the title here</text>
  <text x="108" y="178" text-anchor="middle" font-size="4" class="wh">ADD THE TITLE HERE</text>
  <g>
    <rect x="212" y="70" width="14" height="14" class="dk"/><rect x="212" y="112" width="14" height="14" class="dk"/><rect x="212" y="154" width="14" height="14" class="dk"/><rect x="212" y="196" width="14" height="14" class="dk"/>
    <circle cx="219" cy="77" r="3.5" fill="none" stroke="#fff" stroke-width=".7"/><circle cx="219" cy="119" r="3.5" fill="none" stroke="#fff" stroke-width=".7"/><rect x="215" y="158" width="8" height="6" fill="none" stroke="#fff" stroke-width=".7"/><path d="M214,205 l5,-5 5,5 v4 h-10 Z" fill="none" stroke="#fff" stroke-width=".7"/>
  </g>
  <g font-size="4.4" class="ink">
    <text x="231" y="73" class="bold">Add a title</text><text x="231" y="79">Add your detailed small paragraph text here, and be concise</text><text x="231" y="84">about the title and conform to the overall language style, express</text><text x="231" y="89">the meaning you need to express clearly and completely, and</text><text x="231" y="94">keep it beautiful and generous.</text>
    <text x="231" y="115" class="bold">Add a title</text><text x="231" y="121">Add your detailed small paragraph text here, and be concise</text><text x="231" y="126">about the title and conform to the overall language style, express</text><text x="231" y="131">the meaning you need to express clearly and completely, and</text><text x="231" y="136">keep it beautiful and generous.</text>
    <text x="231" y="157" class="bold">Add a title</text><text x="231" y="163">Add your detailed small paragraph text here, and be concise</text><text x="231" y="168">about the title and conform to the overall language style, express</text><text x="231" y="173">the meaning you need to express clearly and completely, and</text><text x="231" y="178">keep it beautiful and generous.</text>
    <text x="231" y="199" class="bold">Add a title</text><text x="231" y="205">Add your detailed small paragraph text here, and be concise</text><text x="231" y="210">about the title and conform to the overall language style, express</text><text x="231" y="215">the meaning you need to express clearly and completely, and</text><text x="231" y="220">keep it beautiful and generous.</text>
  </g>
</svg>

<svg class="slide services" style="left:318px;top:438px" viewBox="0 0 442 248">
  <rect width="442" height="248" class="wh"/>
  <rect x="22" y="15" width="16" height="10" class="dk"/><text x="30" y="22" text-anchor="middle" font-size="4" class="wh">00</text><text x="42" y="24" font-size="8" class="ink">Heading</text>
  <rect role="img" aria-label="Hands working at a desk, dark green tinted photo" x="0" y="56" width="442" height="94" fill="#1f403b"/>
  <g class="line-or" stroke-width=".9">
    <circle cx="62" cy="103" r="15"/><circle cx="168" cy="103" r="15"/><circle cx="274" cy="103" r="15"/><circle cx="380" cy="103" r="15"/>
    <circle cx="62" cy="100" r="4"/><path d="M58,108 h8"/>
    <rect x="160" y="98" width="16" height="10" rx="2"/><circle cx="168" cy="103" r="2.5"/>
    <circle cx="274" cy="100" r="3"/><path d="M268,110 a6,5 0 0 1 12,0"/>
    <path d="M373,110 v-5 M378,110 v-8 M383,110 v-11 M387,110 v-6"/>
  </g>
  <g text-anchor="middle">
    <g font-size="7.5" class="ink"><text x="62" y="171">Add a title</text><text x="168" y="171">Add a title</text><text x="274" y="171">Add a title</text><text x="380" y="171">Add a title</text></g>
    <g font-size="4.5" class="mu">
      <text x="62" y="182">Add your detailed small</text><text x="62" y="188">paragraph text content</text><text x="62" y="194">here</text>
      <text x="168" y="182">Add your detailed small</text><text x="168" y="188">paragraph text content</text><text x="168" y="194">here</text>
      <text x="274" y="182">Add your detailed small</text><text x="274" y="188">paragraph text content</text><text x="274" y="194">here</text>
      <text x="380" y="182">Add your detailed small</text><text x="380" y="188">paragraph text content</text><text x="380" y="194">here</text>
    </g>
  </g>
</svg>

<svg class="slide cycle" style="left:606px;top:438px" viewBox="0 0 442 248">
  <rect width="442" height="248" class="wh"/>
  <rect x="22" y="15" width="16" height="10" class="dk"/><text x="30" y="22" text-anchor="middle" font-size="4" class="wh">00</text><text x="42" y="24" font-size="8" class="ink">Heading</text>
  <ellipse cx="221" cy="135" rx="48" ry="46" class="line-or" stroke-width=".5"/>
  <circle cx="198" cy="91" r="9" class="or"/><circle cx="173" cy="135" r="9" class="dk"/><circle cx="198" cy="180" r="9" class="or"/>
  <circle cx="244" cy="91" r="9" class="dk"/><circle cx="269" cy="135" r="9" class="or"/><circle cx="244" cy="180" r="9" class="dk"/>
  <g fill="none" stroke="#fff" stroke-width=".7"><circle cx="198" cy="91" r="3.5"/><circle cx="173" cy="135" r="3.5"/><circle cx="198" cy="180" r="3.5"/><path d="M241,88 h6 l-3,6 Z"/><rect x="265" y="132" width="8" height="6"/><path d="M240,184 v-2 M243,184 v-4 M246,184 v-6"/></g>
  <g font-size="4.5" text-anchor="end" class="ink">
    <text x="176" y="88" class="bold">Add a title</text><text x="176" y="94">Add your detailed small paragraph text here, and</text><text x="176" y="100">be concise about the title and conform to the</text><text x="176" y="106">overall language style</text>
    <text x="151" y="132" class="bold">Add a title</text><text x="151" y="138">Add your detailed small paragraph text here, and</text><text x="151" y="144">be concise about the title and conform to the</text><text x="151" y="150">overall language style</text>
    <text x="176" y="177" class="bold">Add a title</text><text x="176" y="183">Add your detailed small paragraph text here, and</text><text x="176" y="189">be concise about the title and conform to the</text><text x="176" y="195">overall language style</text>
  </g>
  <g font-size="4.5" class="ink">
    <text x="266" y="88" class="bold">Add a title</text><text x="266" y="94">Add your detailed small paragraph text here, and</text><text x="266" y="100">be concise about the title and conform to the</text><text x="266" y="106">overall language style</text>
    <text x="291" y="132" class="bold">Add a title</text><text x="291" y="138">Add your detailed small paragraph text here, and</text><text x="291" y="144">be concise about the title and conform to the</text><text x="291" y="150">overall language style</text>
    <text x="266" y="177" class="bold">Add a title</text><text x="266" y="183">Add your detailed small paragraph text here, and</text><text x="266" y="189">be concise about the title and conform to the</text><text x="266" y="195">overall language style</text>
  </g>
</svg>

<svg class="slide progress-rings" style="left:894px;top:438px" viewBox="0 0 442 248">
  <rect width="442" height="248" class="wh"/>
  <rect x="22" y="15" width="16" height="10" class="dk"/><text x="30" y="22" text-anchor="middle" font-size="4" class="wh">00</text><text x="42" y="24" font-size="8" class="ink">Heading</text>
  <g fill="none" stroke-width="1.4">
    <circle cx="75" cy="70" r="22" stroke="#eee"/><circle cx="172" cy="70" r="22" stroke="#eee"/><circle cx="269" cy="70" r="22" stroke="#eee"/><circle cx="366" cy="70" r="22" stroke="#eee"/>
    <g stroke="var(--orange)" stroke-dasharray="113 138">
      <circle cx="75" cy="70" r="22" transform="rotate(-90 75 70)"/><circle cx="172" cy="70" r="22" transform="rotate(-90 172 70)"/><circle cx="269" cy="70" r="22" transform="rotate(-90 269 70)"/><circle cx="366" cy="70" r="22" transform="rotate(-90 366 70)"/>
    </g>
  </g>
  <g text-anchor="middle">
    <g font-size="4.5" class="ink"><text x="75" y="72">82%</text><text x="172" y="72">82%</text><text x="269" y="72">82%</text><text x="366" y="72">82%</text></g>
    <g font-size="4.5" class="ink bold"><text x="75" y="104">Add a title</text><text x="172" y="104">Add a title</text><text x="269" y="104">Add a title</text><text x="366" y="104">Add a title</text></g>
    <g font-size="4.3" class="mu">
      <text x="75" y="111">Add your detailed small</text><text x="75" y="117">paragraph text here, and</text><text x="75" y="123">keep it simple and</text><text x="75" y="129">generous with title-related</text><text x="75" y="135">and overall language style</text><text x="75" y="141">content.</text>
      <text x="172" y="111">Add your detailed small</text><text x="172" y="117">paragraph text here, and</text><text x="172" y="123">keep it simple and</text><text x="172" y="129">generous with title-related</text><text x="172" y="135">and overall language style</text><text x="172" y="141">content.</text>
      <text x="269" y="111">Add your detailed small</text><text x="269" y="117">paragraph text here, and</text><text x="269" y="123">keep it simple and</text><text x="269" y="129">generous with title-related</text><text x="269" y="135">and overall language style</text><text x="269" y="141">content.</text>
      <text x="366" y="111">Add your detailed small</text><text x="366" y="117">paragraph text here, and</text><text x="366" y="123">keep it simple and</text><text x="366" y="129">generous with title-related</text><text x="366" y="135">and overall language style</text><text x="366" y="141">content.</text>
    </g>
  </g>
  <rect x="0" y="150" width="442" height="98" class="dk"/>
  <g text-anchor="middle" class="wh">
    <text x="221" y="175" font-size="10">Add the title here</text>
    <text x="221" y="182" font-size="4">ADD THE TITLE HERE</text>
    <g font-size="4.4"><text x="221" y="198">Add your detailed small paragraph text content here, related to the title and in line with the overall language style content please be concise, as</text><text x="221" y="204">vivid as possible, you need to express the meaning clearly complete, control the number of words, and design layout in line with, to maintain</text><text x="221" y="210">beautiful and generous. Add your detailed small paragraph text content here, related to the title and in line with the overall language style</text><text x="221" y="216">content please be concise, as vivid as possible, you need to express the meaning clearly complete, control the number of words, and design</text><text x="221" y="222">layout in line with, to maintain beautiful and generous</text></g>
  </g>
</svg>

<!-- Row 4 -->
<svg class="slide three-panels" style="left:32px;top:607px" viewBox="0 0 442 248">
  <rect width="442" height="248" class="wh"/>
  <rect x="22" y="15" width="16" height="10" class="dk"/><text x="30" y="22" text-anchor="middle" font-size="4" class="wh">00</text><text x="42" y="24" font-size="8" class="ink">Heading</text>
  <rect x="53" y="55" width="335" height="167" class="dk"/>
  <rect x="160" y="48" width="120" height="180" class="or"/>
  <rect x="69" y="72" width="81" height="54" class="wh"/><rect role="img" aria-label="Charts and documents on desk photo" x="71" y="74" width="77" height="50" fill="url(#office)"/>
  <rect x="180" y="62" width="81" height="54" class="wh"/><rect role="img" aria-label="Hands with laptop photo" x="182" y="64" width="77" height="50" fill="url(#desk)"/>
  <rect x="291" y="72" width="81" height="54" class="wh"/><rect role="img" aria-label="Reports with pen on table photo" x="293" y="74" width="77" height="50" fill="url(#office)"/>
  <g text-anchor="middle" class="wh">
    <text x="109" y="154" font-size="8">Add a title</text>
    <g font-size="4.5"><text x="109" y="166">Add your detailed small</text><text x="109" y="172">paragraph text content</text><text x="109" y="178">here</text></g>
    <text x="220" y="151" font-size="10">Add a title</text>
    <text x="220" y="158" font-size="4">ADD THE TITLE HERE</text>
    <g font-size="4.5"><text x="220" y="174">Add your detailed small paragraph</text><text x="220" y="180">text content here</text></g>
    <text x="332" y="154" font-size="8">Add a title</text>
    <g font-size="4.5"><text x="332" y="166">Add your detailed small</text><text x="332" y="172">paragraph text content</text><text x="332" y="178">here</text></g>
  </g>
</svg>

<svg class="slide barchart" style="left:318px;top:607px" viewBox="0 0 442 248">
  <rect width="442" height="248" class="wh"/>
  <rect x="22" y="15" width="16" height="10" class="dk"/><text x="30" y="22" text-anchor="middle" font-size="4" class="wh">00</text><text x="42" y="24" font-size="8" class="ink">Heading</text>
  <g font-size="4.5" class="ink"><text x="28" y="50">6</text><text x="28" y="76">5</text><text x="28" y="102">4</text><text x="28" y="128">3</text><text x="28" y="154">2</text><text x="28" y="180">1</text><text x="28" y="206">0</text></g>
  <line x1="38" y1="204" x2="215" y2="204" stroke="#ccc" stroke-width=".5"/>
  <g>
    <rect x="45" y="92" width="7" height="112" fill="var(--amber)"/><rect x="54" y="142" width="7" height="62" fill="#f5b800"/><rect x="63" y="152" width="7" height="52" fill="var(--orange-soft)"/>
    <rect x="90" y="139" width="7" height="65" fill="var(--amber)"/><rect x="99" y="90" width="7" height="114" fill="#f5b800"/><rect x="108" y="152" width="7" height="52" fill="var(--orange-soft)"/>
    <rect x="135" y="113" width="7" height="91" fill="var(--amber)"/><rect x="144" y="157" width="7" height="47" fill="#f5b800"/><rect x="153" y="126" width="7" height="78" fill="var(--orange-soft)"/>
    <rect x="180" y="87" width="7" height="117" fill="var(--amber)"/><rect x="189" y="131" width="7" height="73" fill="#f5b800"/><rect x="198" y="74" width="7" height="130" fill="var(--orange-soft)"/>
  </g>
  <g font-size="4" class="ink" text-anchor="middle"><text x="57" y="212">Cat 1</text><text x="102" y="212">Cat 2</text><text x="147" y="212">Cat 3</text><text x="192" y="212">Cat 4</text><text x="126" y="222">■ S1   ■ S2   ■ S3</text></g>
  <g class="line-or" stroke-width="1">
    <circle cx="272" cy="76" r="5"/><circle cx="272" cy="76" r="2"/>
    <circle cx="371" cy="75" r="4"/><path d="M374,78 l5,5"/>
    <circle cx="272" cy="166" r="3"/><path d="M266,174 a6,5 0 0 1 12,0"/>
    <path d="M366,174 v-6 h3 l3,-6 h2 v6 h5 v6 Z"/>
  </g>
  <g text-anchor="middle">
    <g font-size="7.5" class="ink"><text x="272" y="98">Add a title</text><text x="373" y="98">Add a title</text><text x="272" y="189">Add a title</text><text x="373" y="189">Add a title</text></g>
    <g font-size="4.5" class="mu"><text x="272" y="108">Add your detailed small</text><text x="272" y="114">paragraph text here</text><text x="373" y="108">Add your detailed small</text><text x="373" y="114">paragraph text here</text><text x="272" y="199">Add your detailed small</text><text x="272" y="205">paragraph text here</text><text x="373" y="199">Add your detailed small</text><text x="373" y="205">paragraph text here</text></g>
  </g>
</svg>

<svg class="slide icon-list" style="left:606px;top:607px" viewBox="0 0 442 248">
  <rect width="442" height="248" class="wh"/>
  <rect x="22" y="15" width="16" height="10" class="dk"/><text x="30" y="22" text-anchor="middle" font-size="4" class="wh">00</text><text x="42" y="24" font-size="8" class="ink">Heading</text>
  <rect role="img" aria-label="Glass dome architecture photo in teal tones" x="252" y="0" width="190" height="248" fill="url(#teal)"/>
  <g fill="none" stroke="var(--orange)" stroke-width=".9">
    <circle cx="378" cy="58" r="19"/><path d="M368,64 l6,-6 4,4 8,-9"/>
    <circle cx="378" cy="124" r="19"/><circle cx="378" cy="124" r="9"/><path d="M369,124 h18 M378,115 v18"/>
    <circle cx="378" cy="198" r="19"/><path d="M368,206 l20,-16 M372,196 l8,4 M378,202 l4,6"/>
  </g>
  <g fill="none" stroke="var(--orange)" stroke-width=".7">
    <rect x="27" y="58" width="14" height="14"/><rect x="27" y="107" width="14" height="14"/><rect x="27" y="155" width="14" height="14"/><rect x="27" y="204" width="14" height="14"/>
    <path d="M31,68 h6 M31,64 h6"/><circle cx="34" cy="114" r="3"/><path d="M32,159 v6 h4"/><path d="M31,208 l3,4 3,-4 M34,212 v4"/>
  </g>
  <g font-size="4.4" class="ink">
    <text x="46" y="62" class="bold">Add a title</text><text x="46" y="68">Add your detailed small paragraph text here, and be concise</text><text x="46" y="74">about the title and conform to the overall language style</text>
    <text x="46" y="111" class="bold">Add a title</text><text x="46" y="117">Add your detailed small paragraph text here, and be concise</text><text x="46" y="123">about the title and conform to the overall language style</text>
    <text x="46" y="159" class="bold">Add a title</text><text x="46" y="165">Add your detailed small paragraph text here, and be concise</text><text x="46" y="171">about the title and conform to the overall language style</text>
    <text x="46" y="208" class="bold">Add a title</text><text x="46" y="214">Add your detailed small paragraph text here, and be concise</text><text x="46" y="220">about the title and conform to the overall language style</text>
  </g>
</svg>

<svg class="slide pie" style="left:894px;top:607px" viewBox="0 0 442 248">
  <rect role="img" aria-label="Office desk with hands and laptop photo" width="442" height="248" fill="url(#desk)"/>
  <rect x="30" y="44" width="382" height="184" class="dk"/>
  <text x="72" y="87" font-size="10" class="wh">Add the title here</text>
  <text x="72" y="94" font-size="4" class="wh">ADD THE TITLE HERE</text>
  <g font-size="4.5" class="wh">
    <text x="72" y="108">Add your detailed small paragraph text content</text><text x="72" y="114">here, related to the title and in line with the</text><text x="72" y="120">overall language style content please be concise,</text><text x="72" y="126">as vivid as possible, you need to express the</text><text x="72" y="132">meaning clearly complete, control the number</text><text x="72" y="138">of words, and design layout in line with, to</text><text x="72" y="144">maintain beautiful and generous.</text>
  </g>
  <line x1="72" y1="180" x2="86" y2="180" stroke="#889" stroke-width=".5"/>
  <path d="M309,122 L309,77 A45,45 0 1 1 264.7,129.8 Z" class="or"/>
  <path d="M309,122 L264.7,129.8 A45,45 0 0 1 286.5,83 Z" fill="#ec7a2a"/>
  <path d="M309,122 L286.5,83 A45,45 0 0 1 309,77 Z" fill="#8a8a8a"/>
</svg>

<!-- Row 5 -->
<svg class="slide quadrant" style="left:32px;top:777px" viewBox="0 0 442 248">
  <rect width="442" height="248" class="wh"/>
  <rect x="22" y="15" width="16" height="10" class="dk"/><text x="30" y="22" text-anchor="middle" font-size="4" class="wh">00</text><text x="42" y="24" font-size="8" class="ink">Heading</text>
  <rect x="177" y="88" width="42" height="42" rx="14" class="dk"/>
  <rect x="223" y="88" width="42" height="42" rx="14" class="or"/>
  <rect x="177" y="134" width="42" height="42" rx="14" class="or"/>
  <rect x="223" y="134" width="42" height="42" rx="14" class="dk"/>
  <circle cx="221" cy="132" r="10" class="wh"/>
  <g font-size="13" class="wh" text-anchor="middle"><text x="198" y="114">01</text><text x="244" y="114">02</text><text x="198" y="160">03</text><text x="244" y="160">04</text></g>
  <g font-size="4.5" class="ink" text-anchor="end">
    <text x="162" y="91" class="bold">Add a title</text><text x="162" y="97">Add your detailed small paragraph</text><text x="162" y="103">text here</text>
    <text x="162" y="150" class="bold">Add a title</text><text x="162" y="156">Add your detailed small paragraph</text><text x="162" y="162">text here</text>
  </g>
  <g font-size="4.5" class="ink">
    <text x="280" y="91" class="bold">Add a title</text><text x="280" y="97">Add your detailed small paragraph</text><text x="280" y="103">text here</text>
    <text x="280" y="150" class="bold">Add a title</text><text x="280" y="156">Add your detailed small paragraph</text><text x="280" y="162">text here</text>
  </g>
</svg>

<svg class="slide blocks" style="left:321px;top:777px" viewBox="0 0 442 248">
  <rect width="442" height="248" class="wh"/>
  <rect x="22" y="15" width="16" height="10" class="dk"/><text x="30" y="22" text-anchor="middle" font-size="4" class="wh">00</text><text x="42" y="24" font-size="8" class="ink">Heading</text>
  <text x="412" y="74" text-anchor="end" font-size="13" class="ink">Add the title here</text>
  <text x="412" y="82" text-anchor="end" font-size="4.5" class="ink">ADD THE TITLE HERE</text>
  <line x1="345" y1="85" x2="412" y2="85" stroke="#333" stroke-width=".4"/>
  <rect role="img" aria-label="Spiral staircase looking up photo" x="25" y="98" width="167" height="130" fill="url(#desk)"/>
  <rect x="232" y="98" width="87" height="130" class="or"/>
  <rect x="329" y="98" width="87" height="130" class="dk"/>
  <g text-anchor="middle" class="wh">
    <text x="275" y="141" font-size="5" class="bold">Add a title</text>
    <g font-size="4.3"><text x="275" y="149">Add your detailed small</text><text x="275" y="155">paragraph text here, and</text><text x="275" y="161">be concise about the title</text><text x="275" y="167">and conform to the</text><text x="275" y="173">overall language style</text></g>
    <text x="372" y="141" font-size="5" class="bold">Add a title</text>
    <g font-size="4.3"><text x="372" y="149">Add your detailed small</text><text x="372" y="155">paragraph text here, and</text><text x="372" y="161">be concise about the title</text><text x="372" y="167">and conform to the</text><text x="372" y="173">overall language style</text></g>
  </g>
</svg>

<svg class="slide radar" style="left:606px;top:777px" viewBox="0 0 442 248">
  <rect width="442" height="248" class="wh"/>
  <rect x="22" y="15" width="16" height="10" class="dk"/><text x="30" y="22" text-anchor="middle" font-size="4" class="wh">00</text><text x="42" y="24" font-size="8" class="ink">Heading</text>
  <g fill="none" stroke="#ccc" stroke-width=".5">
    <polygon points="119,80 181,125 157,198 81,198 57,125"/>
    <polygon points="119,96 166,130 148,185 90,185 72,130"/>
    <polygon points="119,112 150,135 138,172 100,172 88,135"/>
    <polygon points="119,129 134,140 128,158 110,158 104,140"/>
    <path d="M119,145 L119,80 M119,145 L181,125 M119,145 L157,198 M119,145 L81,198 M119,145 L57,125"/>
  </g>
  <polygon points="119,88 170,128 150,190 110,162 100,140" fill="none" stroke="#1f2a5c" stroke-width=".9"/>
  <polygon points="119,118 140,140 135,170 95,175 80,128" fill="none" stroke="var(--orange)" stroke-width=".9"/>
  <g font-size="4.3" class="ink" text-anchor="middle">
    <text x="119" y="75">2002-01-05</text><text x="116" y="82">40</text><text x="116" y="99">30</text><text x="116" y="115">20</text><text x="116" y="131">10</text><text x="116" y="148">0</text>
    <text x="200" y="126">2002-01-06</text><text x="168" y="206">2002-01-07</text><text x="70" y="206">2002-01-08</text><text x="38" y="126">2002-01-09</text>
  </g>
  <text x="248" y="74" font-size="10" class="ink">Add the title here</text>
  <text x="248" y="81" font-size="4" class="ink">ADD THE TITLE HERE</text>
  <g font-size="4.4" class="mu"><text x="248" y="97">Add your detailed small paragraph text content here,</text><text x="248" y="103">related to the title and in line with the overall language</text><text x="248" y="109">style content please be concise, as vivid as possible, you</text><text x="248" y="115">need to express the meaning clearly complete, control</text><text x="248" y="121">the number of words, and design layout in line with, to</text><text x="248" y="127">maintain beautiful and generous.</text></g>
  <g font-size="5" class="ink"><text x="248" y="143">Add a subheading</text><text x="248" y="175">Add a subheading</text><text x="248" y="206">Add a subheading</text></g>
  <rect x="248" y="154" width="150" height="3" fill="#888"/><rect x="248" y="154" width="118" height="3" class="or"/>
  <rect x="248" y="185" width="150" height="3" fill="#888"/><rect x="248" y="185" width="118" height="3" class="or"/>
  <rect x="248" y="216" width="150" height="3" fill="#888"/><rect x="248" y="216" width="128" height="3" class="or"/>
</svg>

<svg class="slide timeline" style="left:894px;top:777px" viewBox="0 0 442 248">
  <rect width="442" height="248" class="wh"/>
  <rect x="22" y="15" width="16" height="10" class="dk"/><text x="30" y="22" text-anchor="middle" font-size="4" class="wh">00</text><text x="42" y="24" font-size="8" class="ink">Heading</text>
  <line x1="30" y1="101" x2="413" y2="101" stroke="#222" stroke-width="1.2"/>
  <g font-size="6" text-anchor="middle"><text x="68" y="97" class="ink">20XX.04</text><text x="144" y="97" class="or">20XX.06</text><text x="221" y="97" class="ink">20XX.08</text><text x="298" y="97" class="or">20XX.10</text><text x="374" y="97" class="ink">20XX.12</text></g>
  <g stroke="#444" stroke-width=".6" stroke-dasharray="1.5 1.5"><line x1="68" y1="104" x2="68" y2="146"/><line x1="144" y1="104" x2="144" y2="146"/><line x1="221" y1="104" x2="221" y2="146"/><line x1="298" y1="104" x2="298" y2="146"/><line x1="374" y1="104" x2="374" y2="146"/></g>
  <circle cx="68" cy="152" r="6" class="dk"/><circle cx="144" cy="156" r="8" class="or"/><circle cx="221" cy="152" r="6" class="dk"/><circle cx="298" cy="156" r="8" class="or"/><circle cx="374" cy="152" r="6" class="dk"/>
  <g text-anchor="middle" font-size="4.4" class="ink">
    <text x="68" y="165" class="bold">Add a title</text><text x="68" y="171">Add your detailed</text><text x="68" y="177">small paragraph text</text><text x="68" y="183">here</text>
    <text x="144" y="172" class="bold">Add a title</text><text x="144" y="178">Add your detailed</text><text x="144" y="184">small paragraph text</text><text x="144" y="190">here</text>
    <text x="221" y="172" class="bold">Add a title</text><text x="221" y="178">Add your detailed</text><text x="221" y="184">small paragraph text</text><text x="221" y="190">here</text>
    <text x="298" y="172" class="bold">Add a title</text><text x="298" y="178">Add your detailed</text><text x="298" y="184">small paragraph text</text><text x="298" y="190">here</text>
    <text x="374" y="165" class="bold">Add a title</text><text x="374" y="171">Add your detailed</text><text x="374" y="177">small paragraph text</text><text x="374" y="183">here</text>
  </g>
</svg>

<!-- Row 6 -->
<svg class="slide closing" style="left:32px;top:946px" viewBox="0 0 442 248">
  <rect width="442" height="248" class="wh"/>
  <polygon points="0,0 236,0 94,248 0,248" class="dk"/>
  <polygon points="25,80 245,80 196,168 25,168" class="or"/>
  <polygon points="190,80 245,80 196,168 141,168" fill="#f6a623"/>
  <text x="118" y="135" text-anchor="middle" font-size="30" class="wh">Thanks</text>
  <text x="335" y="141" text-anchor="middle" font-size="6.3" letter-spacing="3" textLength="196" lengthAdjust="spacing" class="dk">VYMAR LIFE SCIENCES</text>
  <text x="320" y="151" text-anchor="middle" font-size="3.2" letter-spacing="1" textLength="124" lengthAdjust="spacing" class="dk">QUALITY-LED GROWTH FOR PHARMA AND DEVICES</text>
</svg>

</div>
</body>
</html>
```